Brenvale Services - Fast, Efficient and Gas Mainteance for Domestic, Commercial and Industrial clients

We are in the process of purchasing a new business and would like to get a new logo and business card.
Business is a gas maintenance business that also does new gas installations.
Has been established since 1988.
Services include:
Install all types of gas appliances & equipment inc. hot water units
Maintain / repair / replace all types of gas appliances & equipment

Target Market(s)

Domestic, Commercial and Industrial clients

Industry/Entity Type

Business

Contact Information for Business Card

admin@brenvaleservices.com.au
07 5814 2960
Brenvale Services PTY LTD

Logo Text

Gas Fitting & Plumbing Maintenance Specialists

Font styles to use
Sans Serif

Requirements
Must have
• Logo
• Business name, contact number, email address, web address
• Domestic | Commercial | Industrial Est Since 1988
Nice to have
• Possibly a black card with a flame logo to one side
Should not have
• Spelling errors

```html
<!DOCTYPE html>
<html lang="en">
<head>
<meta charset="utf-8">
<title>Brenvale Services – Business Card</title>
<link rel="stylesheet" href="https://fonts.googleapis.com/css2?family=Montserrat:wght@400;500;800&display=swap">
<style>
  :root {
    --page-bg: #e9eaec;
    --card-bg: #f8f8f7;
    --card-edge: #d6d6d6;
    --ink: #161616;
    --accent: #d9531e;
    --band-start: #e2571c;
    --band-mid: #ef7a1a;
    --band-end: #c91f1c;
    --mark: #e0621e;
  }
  * { margin: 0; padding: 0; box-sizing: border-box; }
  html, body {
    width: 1200px;
    height: 970px;
    overflow: hidden;
    background: var(--page-bg);
    font-family: "Montserrat", sans-serif;
    color: var(--ink);
  }
  .canvas {
    position: relative;
    width: 1200px;
    height: 970px;
  }
  .business-card {
    position: absolute;
    left: 100px;
    top: 208px;
    width: 1000px;
    height: 553px;
    background: var(--card-bg);
    border: 1px solid var(--card-edge);
    border-radius: 26px;
    overflow: hidden;
    box-shadow: 0 18px 40px rgba(0,0,0,0.12);
  }
  .brand {
    position: absolute;
    left: 57px;
    top: 78px;
    display: flex;
    align-items: center;
    gap: 40px;
  }
  .brand-dot {
    width: 140px;
    height: 140px;
    border-radius: 50%;
    background: var(--mark);
  }
  .brand-name {
    font-weight: 800;
    color: var(--ink);
    line-height: 1;
  }
  .brand-name .brand-main {
    display: block;
    font-size: 52px;
    letter-spacing: 2px;
  }
  .brand-name .brand-sub {
    display: block;
    margin-top: 8px;
    font-size: 19px;
    letter-spacing: 3.2px;
  }
  .contact {
    position: absolute;
    left: 236px;
    top: 258px;
  }
  .contact-name {
    font-size: 26px;
    font-weight: 500;
    color: var(--accent);
    margin-bottom: 18px;
  }
  .contact-line {
    display: flex;
    align-items: center;
    gap: 12px;
    font-size: 22px;
    font-weight: 400;
    height: 32px;
  }
  .contact-line svg { width: 20px; height: 20px; flex: none; }
  .services {
    position: absolute;
    left: 236px;
    top: 392px;
    font-size: 22px;
    font-weight: 400;
    line-height: 29px;
  }
  .card-band {
    position: absolute;
    left: 0;
    right: 0;
    bottom: 0;
    height: 27px;
    background: linear-gradient(90deg, var(--band-start) 0%, var(--band-mid) 55%, var(--band-end) 100%);
  }
</style>
</head>
<body>
<main class="canvas">
  <section class="business-card" aria-label="Brenvale Services business card">
    <div class="brand">
      <div class="brand-dot" aria-hidden="true"></div>
      <h1 class="brand-name">
        <span class="brand-main">BRENVALE</span>
        <span class="brand-sub">SERVICES PTY LTD</span>
      </h1>
    </div>

    <div class="contact">
      <p class="contact-name">Dale Hartley</p>
      <p class="contact-line">
        <svg viewBox="0 0 24 24" aria-hidden="true"><path fill="#d9531e" d="M6.6 10.8a15.1 15.1 0 0 0 6.6 6.6l2.2-2.2a1 1 0 0 1 1-.25 11.4 11.4 0 0 0 3.6.57 1 1 0 0 1 1 1V20a1 1 0 0 1-1 1A17 17 0 0 1 3 4a1 1 0 0 1 1-1h3.5a1 1 0 0 1 1 1c0 1.25.2 2.45.57 3.57a1 1 0 0 1-.25 1z"/></svg>
        <span>07 5814 2960</span>
      </p>
      <p class="contact-line">
        <svg viewBox="0 0 24 24" aria-hidden="true"><rect x="2" y="5" width="20" height="14" rx="1" fill="#d9531e"/><path d="M2.5 5.5 12 13l9.5-7.5" fill="none" stroke="#f8f8f7" stroke-width="1.6"/></svg>
        <span>admin@brenvaleservices.com.au</span>
      </p>
    </div>

    <p class="services">
      Install all types of gas appliances &amp;<br>
      equipment inc. hot water units<br>
      Maintain / repair / replace all types of<br>
      gas appliances &amp; equipment
    </p>

    <div class="card-band" aria-hidden="true"></div>
  </section>
</main>
</body>
</html>
```